Marlowen Promotional Flier

1 page flier that can be emailed to perspective customers or printed and distributed. Flier should use logo and design cues from our website, marlowen.example. We offer equipment financing and business loans to small businesses. The design should incorporate the highlights of working with Marlowen which include:

Benefits:
- Approvals In Hours
- Automated, Easy Application Process
- New and Used Equipment Financed
- 92% Approval Rate
-Flexible Terms
- Superior Support

Program Minimums:
- 450 Minimum Credit Score
- 2 months minimum Time In Business
- $7,500/mo minimum revenue deposits

Target Market(s)

Small To Medium Sized businesses

Industry/Entity Type

Finance

Font styles to use
Sans Serif

Colors
0555a3
3075b4
85acd3
cfdeed

Requirements
Should not have
• No cheesy money bags or dollar signs fling aorund. Should be professional

```html
<!DOCTYPE html>
<html lang="en">
<head>
<meta charset="utf-8">
<title>Marlowen Promotional Flier</title>
<link href="https://fonts.googleapis.com/css2?family=Montserrat:wght@500;600;800&family=Lato:wght@400&family=Oswald:wght@600;700&display=swap" rel="stylesheet">
<style>
  :root {
    --brand-blue: #0555a3;
    --mid-blue: #3075b4;
    --light-blue: #85acd3;
    --pale-blue: #cfdeed;
    --deep-navy: #0d1f4a;
    --program-green: #1d5a13;
    --ink: #1f2933;
    --backdrop: #2a2a2a;
    --white: #ffffff;
  }
  * { box-sizing: border-box; margin: 0; padding: 0; }
  html, body { width: 1200px; height: 1200px; overflow: hidden; background: var(--backdrop); }
  .flier {
    position: absolute; left: 172px; top: 0;
    width: 842px; height: 1180px;
    transform: scale(1.01695); transform-origin: top left;
    background: linear-gradient(180deg, #ffffff 0%, #f1f2f4 45%, #e9eaec 70%, #ffffff 100%);
    overflow: hidden;
  }
  /* Header */
  .hero {
    position: absolute; left: 0; top: 0; width: 842px; height: 348px;
    background: var(--brand-blue);
    background: linear-gradient(180deg, #2a6db5 0%, #1e64b0 100%);
    text-align: center; color: var(--white);
  }
  .hero-photo {
    position: absolute; left: 400px; top: 0; width: 400px; height: 348px;
    background: linear-gradient(90deg, rgba(30,100,176,0) 0%, rgba(20,80,160,0.55) 45%, rgba(30,100,176,0) 100%);
  }
  .hero-title {
    position: relative; padding-top: 98px;
    font: 800 51px/1 "Montserrat", sans-serif; letter-spacing: 1px;
  }
  .hero-sub {
    position: relative; margin-top: 20px;
    font: 500 31px/1 "Montserrat", sans-serif; letter-spacing: 1.5px;
  }
  .cta {
    position: absolute; left: 273px; top: 232px; width: 294px; height: 76px;
    border: 3px solid var(--white);
    font: 600 31px/70px "Montserrat", sans-serif; letter-spacing: 2px; color: var(--white);
  }
  /* Section headings */
  .section-heading {
    position: absolute; left: 0; width: 842px; height: 40px;
  }
  .section-heading .rule {
    position: absolute; top: 50%; height: 2px; background: var(--brand-blue);
  }
  .section-heading .label {
    position: absolute; top: 0; height: 40px;
    font: 600 31px/40px "Montserrat", sans-serif; letter-spacing: 1px;
    color: var(--white); text-align: center; background: var(--brand-blue);
  }
  .benefits-heading { top: 361px; }
  .benefits-heading .rule { left: 132px; width: 550px; }
  .benefits-heading .label { left: 312px; width: 182px; height: 38px; line-height: 38px; }
  .programs-heading { top: 553px; height: 46px; }
  .programs-heading .rule { left: 130px; width: 552px; background: var(--program-green); }
  .programs-heading .label { left: 210px; width: 404px; height: 46px; line-height: 48px; background: var(--program-green); }
  .about-heading { top: 867px; }
  .about-heading .rule { left: 132px; width: 550px; }
  .about-heading .label { left: 314px; width: 196px; height: 38px; line-height: 40px; }
  /* Benefits list */
  .benefit {
    position: absolute; display: flex; align-items: flex-start; gap: 7px;
    font: 400 16px/20px "Lato", sans-serif; color: var(--ink);
  }
  .benefit svg { flex: none; margin-top: 1px; }
  /* Minimum badges */
  .badge {
    position: absolute; width: 192px; height: 192px; border-radius: 50%;
    border: 7px solid var(--deep-navy);
    display: flex; flex-direction: column; align-items: center; justify-content: center;
    color: var(--white); text-align: center; font-family: "Oswald", sans-serif; font-weight: 700;
    text-transform: uppercase; line-height: 1.05;
    box-shadow: 0 3px 8px rgba(0,0,0,0.3);
  }
  .badge-blue { background: radial-gradient(circle at 50% 30%, #3f8ee8 0%, #1b63c9 55%, #1448a0 100%); }
  .badge-green { border-color: #0f2a0a; background: radial-gradient(circle at 50% 30%, #49b83a 0%, #2a8a1d 55%, #1b6112 100%); }
  .badge .figure { font-size: 38px; margin-bottom: 8px; }
  .badge .caption { font-size: 24px; font-weight: 600; }
  /* About */
  .about-copy {
    position: absolute; left: 55px; top: 922px; width: 770px;
    font: 400 15.6px/19.8px "Lato", sans-serif; color: var(--ink);
  }
  /* Footer */
  .footer {
    position: absolute; left: 0; top: 1056px; width: 842px; height: 124px;
    background: linear-gradient(180deg, #1f5fb3 0%, #1452a6 100%); color: var(--white);
  }
  .footer-photo {
    position: absolute; left: 260px; top: 0; width: 420px; height: 124px;
    background: radial-gradient(ellipse at 50% 40%, rgba(120,160,220,0.35) 0%, rgba(31,95,179,0) 70%);
  }
  .wordmark {
    position: absolute; left: 38px; top: 24px;
    font: 600 48px/1 "Montserrat", sans-serif; letter-spacing: -1px; color: var(--white);
  }
  .contact { position: absolute; left: 336px; top: 34px; }
  .contact-line { font: 600 16px/1 "Montserrat", sans-serif; }
  .address-line { margin-top: 10px; font: 400 16px/1 "Lato", sans-serif; }
</style>
</head>
<body>
<div class="flier">
  <header class="hero">
    <div class="hero-photo" role="img" aria-label="Photo of a glass office tower tinted blue"></div>
    <h1 class="hero-title">FAST. EASY. FINANCING</h1>
    <p class="hero-sub">UP TO $2,000,000 IN HOURS, NOT DAYS</p>
    <div class="cta">GET STARTED</div>
  </header>

  <div class="section-heading benefits-heading"><div class="rule"></div><h2 class="label">BENEFITS</h2></div>

  <div class="benefit" style="left:30px;top:424px"><svg width="18" height="18" viewBox="0 0 18 18"><circle cx="9" cy="9" r="8" fill="none" stroke="#0555a3" stroke-width="1.3"/><path d="M5.5 9.2l2.4 2.3 4.6-4.8" fill="none" stroke="#0555a3" stroke-width="1.5"/></svg><span>Approvals In Hours</span></div>
  <div class="benefit" style="left:294px;top:424px"><svg width="18" height="18" viewBox="0 0 18 18"><circle cx="9" cy="9" r="8" fill="none" stroke="#0555a3" stroke-width="1.3"/><path d="M5.5 9.2l2.4 2.3 4.6-4.8" fill="none" stroke="#0555a3" stroke-width="1.5"/></svg><span>Automated, Easy<br>Application Process</span></div>
  <div class="benefit" style="left:590px;top:424px"><svg width="18" height="18" viewBox="0 0 18 18"><circle cx="9" cy="9" r="8" fill="none" stroke="#0555a3" stroke-width="1.3"/><path d="M5.5 9.2l2.4 2.3 4.6-4.8" fill="none" stroke="#0555a3" stroke-width="1.5"/></svg><span>News and used<br>Equipment Financed</span></div>
  <div class="benefit" style="left:30px;top:485px"><svg width="18" height="18" viewBox="0 0 18 18"><circle cx="9" cy="9" r="8" fill="none" stroke="#0555a3" stroke-width="1.3"/><path d="M5.5 9.2l2.4 2.3 4.6-4.8" fill="none" stroke="#0555a3" stroke-width="1.5"/></svg><span>92% Approval Rate</span></div>
  <div class="benefit" style="left:294px;top:485px"><svg width="18" height="18" viewBox="0 0 18 18"><circle cx="9" cy="9" r="8" fill="none" stroke="#0555a3" stroke-width="1.3"/><path d="M5.5 9.2l2.4 2.3 4.6-4.8" fill="none" stroke="#0555a3" stroke-width="1.5"/></svg><span>Flexible Terms</span></div>
  <div class="benefit" style="left:590px;top:485px"><svg width="18" height="18" viewBox="0 0 18 18"><circle cx="9" cy="9" r="8" fill="none" stroke="#0555a3" stroke-width="1.3"/><path d="M5.5 9.2l2.4 2.3 4.6-4.8" fill="none" stroke="#0555a3" stroke-width="1.5"/></svg><span>Superior Support</span></div>

  <div class="section-heading programs-heading"><div class="rule"></div><h2 class="label">PROGRAM MINIMUMS</h2></div>

  <div class="badge badge-blue" style="left:50px;top:639px"><span class="figure">450</span><span class="caption">Minimum<br>Credit Score</span></div>
  <div class="badge badge-green" style="left:333px;top:639px"><span class="figure">2 Months</span><span class="caption">Minimum Time<br>In Business</span></div>
  <div class="badge badge-blue" style="left:601px;top:639px"><span class="figure" style="font-size:34px">$7,500/MO</span><span class="caption" style="font-size:22px">Minimum Revenue<br>Deposits</span></div>

  <div class="section-heading about-heading"><div class="rule"></div><h2 class="label">ABOUT US</h2></div>

  <p class="about-copy">Marlowen was started by a team of financing veterans who knew we could do it smarter, faster, and better. We grew tired of hearing customers’ complaints about endless phone calls from pushy sales people. We knew rates could be made more affordable. We never saw a need for tricky paperwork or hidden fees. So we set out with a simple idea: provide customers with the business financing they need, at the rates they want, with the experience they deserve. 10 years later, Marlowen has helped thousands of businesses access millions of dollars.</p>

  <footer class="footer">
    <div class="footer-photo" role="img" aria-label="Photo of a desk with a laptop and keyboard tinted blue"></div>
    <div class="wordmark">Marlowen</div>
    <div class="contact">
      <p class="contact-line">(888) 555-0142 | info@marlowen.example | marlowen.example</p>
      <p class="address-line">4410 Harbor Lane Ste. 210, Bayview, California 90000</p>
    </div>
  </footer>
</div>
</body>
</html>
```